Business Card Design for Cybersecurity Company - Quorvent Systems

We need a business card design for our new cybersecurity company, Quorvent. We’re going for a clean, hi tech look that feels modern, premium, and trustworthy. We want a design that really stands out and makes people say WOW when we hand it over!

Quorvent delivers reliable IT support and managed services for small and mid sized businesses. We help companies stay secure, efficient, and connected through proactive monitoring, cybersecurity services, cloud management, and remote support.

Target Market(s)

Designers should target small and mid sized businesses that need dependable cybersecurity and IT support.

Industry/Entity Type

Cybersecurity, Managed Service Provider, IT services

Contact Information for Business Card

Contact information

Requirements
Must have
• The card should look clean, modern, and tech focused, with the Quorvent logo, clear contact info, and strong readability. It needs to feel premium and professional while still keeping a simple layout that fits a cybersecurity and IT brand.
Nice to have
• Nice to have elements include subtle touches that give the card a modern, tech feel, along with a layout that works well in different background styles.
Should not have
• The card should avoid clutter, loud graphics, or anything that takes attention away from the logo and contact details.

```html
<!DOCTYPE html>
<html lang="en">
<head>
<meta charset="UTF-8">
<title>Quorvent Systems – Business Card</title>
<link href="https://fonts.googleapis.com/css2?family=Poppins:wght@400;500;600;700&display=swap" rel="stylesheet">
<style>
  :root {
    --page-bg: #2a2b2f;
    --card-dark: #222326;
    --card-dark-2: #2b2c30;
    --card-light: #ffffff;
    --brand-blue: #2a8cf6;
    --brand-violet: #7b2fe0;
    --brand-indigo: #4a3ee8;
    --ink: #3a3a3d;
    --ink-light: #ffffff;
  }
  * { box-sizing: border-box; margin: 0; padding: 0; }
  html, body {
    width: 1200px; height: 952px; overflow: hidden;
    background: var(--page-bg);
    font-family: "Poppins", sans-serif;
  }
  .canvas {
    width: 1200px; height: 952px;
    display: flex; flex-direction: column;
    align-items: center; justify-content: center; gap: 56px;
  }
  .card {
    width: 612px; height: 350px;
    border-radius: 6px;
    position: relative; overflow: hidden;
    box-shadow: 0 18px 40px rgba(0,0,0,.45);
  }

  /* Front */
  .card--front { background: var(--card-dark); }
  .card__texture {
    position: absolute; inset: 0;
    background: radial-gradient(ellipse at 40% 45%, var(--card-dark-2) 0%, var(--card-dark) 70%);
  }
  .brand {
    position: absolute; inset: 0;
    display: flex; align-items: center; justify-content: center; gap: 16px;
  }
  .brand__mark {
    width: 22px; height: 22px;
    background: var(--brand-indigo);
    border-radius: 3px;
  }
  .brand__name {
    color: var(--ink-light);
    font-weight: 600; font-size: 40px; letter-spacing: .5px;
  }

  /* Back */
  .card--back { background: var(--card-light); }
  .identity {
    position: absolute; top: 46px; right: 44px; text-align: right;
  }
  .identity__name {
    font-weight: 700; font-size: 34px; line-height: 1.1;
  }
  .identity__first { color: var(--brand-blue); }
  .identity__last { color: var(--brand-violet); }
  .identity__title {
    margin-top: 6px;
    color: var(--ink); font-size: 13px; font-weight: 400;
  }
  .contact {
    position: absolute; left: 44px; bottom: 56px;
    list-style: none;
    display: flex; flex-direction: column; gap: 10px;
  }
  .contact__item {
    display: flex; align-items: center; gap: 10px;
    color: var(--ink); font-size: 13px;
  }
  .contact__icon {
    width: 20px; height: 20px; border-radius: 4px;
    display: flex; align-items: center; justify-content: center;
    flex: none;
  }
  .contact__icon--blue { background: var(--brand-blue); }
  .contact__icon--indigo { background: var(--brand-indigo); }
  .contact__icon--violet { background: var(--brand-violet); }
  .contact__icon svg { width: 12px; height: 12px; }
  .accent-line {
    position: absolute; right: 44px; bottom: 56px;
    width: 180px; height: 3px; border-radius: 2px;
    background: linear-gradient(90deg, var(--brand-violet), var(--brand-blue));
  }
</style>
</head>
<body>
<main class="canvas">

  <section class="card card--front" aria-label="Business card front">
    <div class="card__texture" role="img" aria-label="Faint circuit-trace pattern on dark background"></div>
    <div class="brand">
      <span class="brand__mark"></span>
      <span class="brand__name">Quorvent Systems</span>
    </div>
  </section>

  <section class="card card--back" aria-label="Business card back">
    <div class="identity">
      <h1 class="identity__name"><span class="identity__first">Dana</span> <span class="identity__last">Whitmore</span></h1>
      <p class="identity__title">Owner | CEO | Quorvent Systems</p>
    </div>

    <ul class="contact">
      <li class="contact__item">
        <span class="contact__icon contact__icon--blue">
          <svg viewBox="0 0 24 24" fill="#fff"><path d="M6.6 10.8a15 15 0 0 0 6.6 6.6l2.2-2.2a1 1 0 0 1 1-.25 11.4 11.4 0 0 0 3.6.57 1 1 0 0 1 1 1V20a1 1 0 0 1-1 1A17 17 0 0 1 3 4a1 1 0 0 1 1-1h3.5a1 1 0 0 1 1 1c0 1.25.2 2.45.57 3.57a1 1 0 0 1-.25 1z"/></svg>
        </span>
        (555) 210-QUOR
      </li>
      <li class="contact__item">
        <span class="contact__icon contact__icon--blue">
          <svg viewBox="0 0 24 24" fill="#fff"><path d="M6.6 10.8a15 15 0 0 0 6.6 6.6l2.2-2.2a1 1 0 0 1 1-.25 11.4 11.4 0 0 0 3.6.57 1 1 0 0 1 1 1V20a1 1 0 0 1-1 1A17 17 0 0 1 3 4a1 1 0 0 1 1-1h3.5a1 1 0 0 1 1 1c0 1.25.2 2.45.57 3.57a1 1 0 0 1-.25 1z"/></svg>
        </span>
        (555) 384-2917
      </li>
      <li class="contact__item">
        <span class="contact__icon contact__icon--indigo">
          <svg viewBox="0 0 24 24" fill="none" stroke="#fff" stroke-width="2.2"><rect x="3" y="5" width="18" height="14" rx="1.5"/><path d="M3 6l9 7 9-7"/></svg>
        </span>
        dana@quorvent.com
      </li>
      <li class="contact__item">
        <span class="contact__icon contact__icon--violet">
          <svg viewBox="0 0 24 24" fill="#fff"><path d="M5 3l14 7-6 2-2 6z"/></svg>
        </span>
        quorvent.com
      </li>
    </ul>

    <div class="accent-line"></div>
  </section>

</main>
</body>
</html>
```